Business Card for a Mortgage Agent (myself)

I need a business card for my new job as Mortgage Agent. The Broker's logo is to be on the card as well as the brokerage License number. Not sure if to include a photo or not. Info to be on card.
Dante Roux
Mortgage Agent
Lic # M47105386
Cell: 905-614-2753
Email: danterouxk.ma@fennmail.com
Web: www.karlvostermortgages.com
TPW Brokerage Lic. # 73918

```html
<!DOCTYPE html>
<html lang="en">
<head>
<meta charset="utf-8">
<title>Dante Roux – Mortgage Agent Business Card</title>
<link href="https://fonts.googleapis.com/css2?family=Open+Sans:wght@400;600;700&display=swap" rel="stylesheet">
<style>
  :root {
    --stage: #3a3a3a;
    --card-dark: #1c1c1c;
    --card-dark-2: #262626;
    --map-tone: #333333;
    --green: #78c143;
    --white: #ffffff;
    --ink: #1a1a1a;
    --ink-soft: #555555;
    --muted: #9a9a9a;
  }
  * { margin: 0; padding: 0; box-sizing: border-box; }
  html, body {
    width: 1200px; height: 900px; overflow: hidden;
    background: var(--stage);
    font-family: "Open Sans", Arial, sans-serif;
  }
  .canvas {
    position: relative; width: 1200px; height: 900px;
    display: flex; flex-direction: column; align-items: center; justify-content: center; gap: 34px;
  }
  .card {
    position: relative; width: 700px; height: 400px; overflow: hidden;
    border-radius: 6px;
    background: linear-gradient(135deg, var(--card-dark-2), var(--card-dark));
    box-shadow: 0 12px 30px rgba(0,0,0,.35);
  }
  .card__shape { position: absolute; inset: 0; width: 100%; height: 100%; }

  /* Front */
  .brand {
    position: absolute; left: 36px; top: 150px;
    display: flex; align-items: center; gap: 14px;
  }
  .brand__square { width: 34px; height: 34px; background: var(--green); flex: none; }
  .brand__text { display: flex; flex-direction: column; gap: 8px; }
  .brand__name {
    color: var(--white); font-weight: 700; font-size: 26px; letter-spacing: 1px; line-height: 1;
    white-space: nowrap;
  }
  .brand__role {
    color: var(--muted); font-size: 11px; letter-spacing: 4px; text-transform: uppercase;
    line-height: 1; white-space: nowrap;
  }
  .contact-icons {
    position: absolute; left: 328px; top: 170px;
    display: flex; flex-direction: column; gap: 15px;
  }
  .contact-icons svg { width: 14px; height: 14px; display: block; }
  .details { position: absolute; left: 380px; top: 70px; color: var(--ink); white-space: nowrap; }
  .details__name { font-size: 36px; font-weight: 700; line-height: 40px; }
  .details__role { color: var(--green); font-size: 16px; font-weight: 600; line-height: 22px; margin-bottom: 30px; }
  .details__line { font-size: 16px; font-weight: 600; line-height: 29px; }
  .details__licence { margin-top: 14px; }
  .details__licence-line { font-size: 13px; font-weight: 600; line-height: 21px; color: var(--ink-soft); }

  /* Back */
  .world-map {
    position: absolute; left: 200px; top: 20px; width: 420px; height: 260px;
    background: radial-gradient(ellipse at center, var(--map-tone) 0%, rgba(51,51,51,0) 72%);
  }
  .back-mark {
    position: absolute; left: 0; right: 0; top: 140px;
    display: flex; justify-content: center; align-items: center; gap: 12px;
  }
  .back-mark__square { width: 26px; height: 26px; background: var(--green); }
  .back-mark__name { color: var(--green); font-size: 24px; font-weight: 700; letter-spacing: 1px; white-space: nowrap; }
  .back-url {
    position: absolute; right: 40px; top: 309px;
    color: var(--white); font-size: 15px; font-weight: 600; white-space: nowrap;
  }
</style>
</head>
<body>
<main class="canvas">

  <section class="card card--front" aria-label="Card front">
    <svg class="card__shape" viewBox="0 0 700 400" preserveAspectRatio="none" aria-hidden="true">
      <path d="M330 0 H700 V400 H290 V150 C290 120 300 95 330 80 Z" fill="#78c143"/>
      <path d="M350 0 H700 V400 H315 V165 C315 135 325 112 350 100 Z" fill="#ffffff"/>
    </svg>

    <div class="brand">
      <span class="brand__square"></span>
      <div class="brand__text">
        <span class="brand__name">DANTE ROUX</span>
        <span class="brand__role">Mortgage Agent</span>
      </div>
    </div>

    <div class="contact-icons" aria-hidden="true">
      <svg viewBox="0 0 16 16"><path d="M8 1a5 5 0 0 0-5 5c0 4 5 9 5 9s5-5 5-9a5 5 0 0 0-5-5zm0 7a2 2 0 1 1 0-4 2 2 0 0 1 0 4z" fill="#fff"/></svg>
      <svg viewBox="0 0 16 16"><path d="M4 1l3 3-2 2c1 2 3 4 5 5l2-2 3 3-2 2C7 14 2 9 2 3z" fill="#fff"/></svg>
      <svg viewBox="0 0 16 16"><circle cx="8" cy="8" r="6" fill="none" stroke="#fff" stroke-width="1.6"/><path d="M2 8h12M8 2c-3 3-3 9 0 12M8 2c3 3 3 9 0 12" fill="none" stroke="#fff" stroke-width="1.2"/></svg>
      <svg viewBox="0 0 16 16"><rect x="1.5" y="3.5" width="13" height="9" fill="none" stroke="#fff" stroke-width="1.6"/><path d="M1.5 3.5l6.5 5 6.5-5" fill="none" stroke="#fff" stroke-width="1.6"/></svg>
    </div>

    <div class="details">
      <div class="details__name">Dante Roux</div>
      <div class="details__role">Mortgage Agent</div>
      <div class="details__line">Southern Ontario</div>
      <div class="details__line">905-614-2753</div>
      <div class="details__line">www.karlvostermortgages.com</div>
      <div class="details__line">danterouxk.ma@fennmail.com</div>
      <div class="details__licence">
        <div class="details__licence-line">Lic # M47105386</div>
        <div class="details__licence-line">TPW Brokerage Lic. # 73918</div>
      </div>
    </div>
  </section>

  <section class="card card--back" aria-label="Card back">
    <div class="world-map" role="img" aria-label="Faint dotted world map in dark grey"></div>
    <svg class="card__shape" viewBox="0 0 700 400" preserveAspectRatio="none" aria-hidden="true">
      <path d="M0 300 H160 C185 300 190 285 215 285 H260 C285 285 290 300 315 300 H700 V340 H0 Z" fill="#78c143"/>
    </svg>
    <div class="back-mark">
      <span class="back-mark__square"></span>
      <span class="back-mark__name">DANTE ROUX</span>
    </div>
    <div class="back-url">www.karlvostermortgages.com</div>
  </section>

</main>
</body>
</html>
```